KVORB Student Exchange needs a brochure design

I need a brochure design for KVORB Student Exchange based in Auckland, New Zealand. I am responsible for outbound exchanges where I recruit local students from around New Zealand between the ages of 15 and 18 who are interested in going on an exchange overseas. Students can select from 12 different countries including America, France, Italy, the Netherlands, Spain, Ireland, Germany, Brazil Japan, and Argentina and choose the programme length from 3 months to an academic year (although we offer shorter programmes for some countries). I would like to attract students who are keen to learn about other cultures and experience something completely different to home. I would like to see vibrant colours and images that coveys fun, youthfulness and adventure.
Updates

Hi,

I have added pics and content for your viewing. 

Thanks.

Tessa

Hi,

Could I request that the designs are done on a tri-fold brochure

Also, I would like to see vibrant colours. So far, I have seen colours matching the logo (which is ok)  but I want to try and move away from that and start something fresh. Please look at the booklet and fee sheet which I have uploaded for ideas. 

I am wondering whether there is too much writing to fit on a tri fold brochure...
If you are having problems fitting everything in, please let me know.

I think the testimonial section could use up 2 spaces on the brochure. 

Target Market(s)

I would like to target teenagers who are interested in other cultures and want to enhance their language learning

Industry/Entity Type

Learn

Font styles to use
Serif
Sans Serif
Decorative

```html
<!DOCTYPE html>
<html lang="en">
<head>
<meta charset="utf-8">
<title>KVORB Student Exchange — Brochure Inside Spread</title>
<link href="https://fonts.googleapis.com/css2?family=Bebas+Neue&family=Lato:wght@400;700&display=swap" rel="stylesheet">
<style>
  :root {
    --teal: #1b8a7e;
    --teal-deep: #16776c;
    --purple: #6a5aa6;
    --ink: #111111;
    --body-grey: #5a5a5a;
    --accent-green: #1c8a48;
    --paper: #ffffff;
    --paper-shade: #ececec;
    --sky-light: #dfe9f6;
    --sky-mid: #8fb0dc;
    --black: #000000;
  }
  * { margin: 0; padding: 0; box-sizing: border-box; }
  html, body { width: 1200px; height: 848px; overflow: hidden; background: var(--paper); }
  .brochure {
    position: relative;
    width: 1200px;
    height: 848px;
    overflow: hidden;
    background: linear-gradient(90deg, var(--paper) 35%, var(--paper-shade) 70%, var(--paper) 100%);
    font-family: "Lato", Arial, sans-serif;
  }
  .brochure__shapes { position: absolute; inset: 0; width: 1200px; height: 848px; }
  .headline {
    position: absolute;
    left: 423px;
    top: 16px;
    font-family: "Bebas Neue", Impact, sans-serif;
    font-size: 44px;
    line-height: 36px;
    color: var(--purple);
    letter-spacing: 0.5px;
  }
  .column { position: absolute; }
  .column__title {
    font-family: "Bebas Neue", Impact, sans-serif;
    font-weight: 400;
    font-size: 37px;
    line-height: 1;
    text-align: center;
    color: var(--ink);
    letter-spacing: 0.3px;
  }
  .column__text {
    font-size: 13.2px;
    line-height: 18.4px;
    color: var(--body-grey);
    text-align: justify;
    text-align-last: center;
  }
  .column__text + .column__text { margin-top: 18px; }
  .column--intro { left: 37px; top: 144px; width: 315px; }
  .column--intro .column__title { color: var(--paper); margin-bottom: 14px; }
  .column--intro .column__text { color: var(--paper); }
  .column--middle { left: 446px; top: 275px; width: 315px; }
  .column--right { left: 827px; top: 275px; width: 315px; }
  .column--middle .column__title,
  .column--right .column__title { margin-bottom: 28px; }
  .column__highlight { color: var(--accent-green); }
</style>
</head>
<body>
<main class="brochure">
  <svg class="brochure__shapes" viewBox="0 0 950 671" preserveAspectRatio="none" aria-hidden="false">
    <defs>
      <linearGradient id="skyTone" x1="0" y1="0" x2="0" y2="1">
        <stop offset="0" stop-color="#7fa3d6"/>
        <stop offset="1" stop-color="#e4edf8"/>
      </linearGradient>
      <linearGradient id="friendsTone" x1="0" y1="0" x2="1" y2="1">
        <stop offset="0" stop-color="#b9866a"/>
        <stop offset="0.5" stop-color="#d9a48f"/>
        <stop offset="1" stop-color="#7d8fa8"/>
      </linearGradient>
      <linearGradient id="studentsTone" x1="0" y1="0" x2="1" y2="1">
        <stop offset="0" stop-color="#c99a7a"/>
        <stop offset="0.55" stop-color="#e2bfa4"/>
        <stop offset="1" stop-color="#8aa0c2"/>
      </linearGradient>
      <linearGradient id="flagsTone" x1="0" y1="0" x2="1" y2="1">
        <stop offset="0" stop-color="#9ab6e0"/>
        <stop offset="0.5" stop-color="#c8463d"/>
        <stop offset="1" stop-color="#3f5fa8"/>
      </linearGradient>
    </defs>

    <g class="sky-band" role="img" aria-label="Bright blue sky with soft white clouds">
      <polygon points="0,0 950,0 950,20 630,158 318,80 0,18" fill="url(#skyTone)"/>
    </g>

    <polygon class="teal-panel" points="0,18 318,80 318,671 0,671" fill="var(--teal)"/>

    <polygon class="corner-accent" points="862,45 950,2 950,103" fill="var(--black)"/>

    <g class="photo photo--friends" role="img" aria-label="Photo of a smiling group of teenage friends posing together">
      <polygon points="535,12 712,12 712,124 630,158 535,134" fill="url(#friendsTone)"/>
    </g>

    <g class="photo photo--students" role="img" aria-label="Photo of laughing students taking a selfie together">
      <polygon points="0,405 352,671 0,671" fill="url(#studentsTone)"/>
    </g>

    <g class="photo photo--flags" role="img" aria-label="Photo of international flags flying on poles against a blue sky">
      <polygon points="400,671 950,478 950,671" fill="url(#flagsTone)"/>
    </g>
  </svg>

  <h1 class="headline">It's time&nbsp; to make<br>new friends</h1>

  <section class="column column--intro">
    <h2 class="column__title">Lorem ipsum dolor</h2>
    <p class="column__text">consectetur adipiscing elit. Mauris feugiat ante a augue vestibulum, et ultrices massa congue. Vestibulum arcu mauris, interdum convallis placerat id, pretium vitae diam. Maecenas vel viverra elit, eu bibendum lorem. Pellentesque habitant morbi tristique senectus et netus et malesuada fames ac turpis egestas. Duis quis elementum urna. Sed ac diam aliquet, suscipit sapien eleifend, tempus augue. Etiam sagittis, nulla nec imperdiet luctus, tortor libero commodo nibh, ut convallis purus arcu non odio. Donec a ipsum ac urna dapibus luctus. Proin dignissim sollicitudin semper. Quisque fermentum dapibus scelerisque.</p>
  </section>

  <section class="column column--middle">
    <h2 class="column__title">Curabitur accumsan quis</h2>
    <p class="column__text">Aenean pulvinar nisi mi, ultrices pellentesque purus dictum eu. Vestibulum varius ante in nisi vestibulum, vel adipiscing tellus placerat. Nullam vehicula, orci sed ultrices suscipit, neque tortor egestas nunc, id ultrices mauris velit et mauris. Fusce nec scelerisque ante. Aenean tempor luctus tincidunt. Duis cursus interdum dignissim. Aenean sagittis urna volutpat quam varius vulputate.</p>
    <p class="column__text">Aenean feugiat sit amet velit eu mattis. Etiam sit amet ligula ligula. Mauris quis ligula bibendum sapien aliquam gravida vitae id arcu. Aliquam tortor nibh, iaculis sit amet suscipit eu, vestibulum vitae metus. Pellentesque eget convallis elit. Nam sit amet dapibus nulla. In hac habitasse platea dictumst.</p>
  </section>

  <section class="column column--right">
    <h2 class="column__title">Nin faucibus.</h2>
    <p class="column__text">Nullam lorem est, tincidunt vel tincidunt a, molestie a mauris. Curabitur accumsan quis magna vehicula dignissim. Pellentesque varius felis at nisl ultricies tempor at at nulla. Fusce eget massa quis leo laoreet elementum vitae eget dui. Cras tristique ultricies gravida. Duis tortor nisi, tristique ac orci ut, dictum pellentesque elit. Quisque sed blandit mi, vitae ornare mi. In hac habitasse platea dictumst. Etiam non tortor porttitor, lacinia neque vitae, feugiat diam. Praesent suscipit, ipsum non <span class="column__highlight">condimentum mattis, mi diam convallis dui, sed porta felis neque volutpat quam</span>.</p>
  </section>
</main>
</body>
</html>
```